Protrait photographers business card

Need a new catchy, chic business card to promote my new portrait photograghy business. Love taking the natural, location portraits of families, children, teens. It should look classy, but also warm & friendly. I want it to show that Famliy, friends, couples & childten are what I love photographing, so if it can have that sort of feel to it & also looking energetic.

Target Market(s)

Families, couples, babies, people on holidays wanting some locational professional photos

Industry/Entity Type

Portrait Photography

Contact Information for Business Card

Lumivale photography, By Tavi, Norah Balfrey,Ph: 0487356024, Kestrel cove, Qld

Font styles to use
Decorative
Script

Requirements
Must have
• Company name & photographers name
Nice to have
• a coloured card
Should not have
• not be on a white card

```html
<!DOCTYPE html>
<html lang="en">
<head>
<meta charset="utf-8">
<title>Lumivale Photography – Business Card</title>
<link rel="stylesheet" href="https://fonts.googleapis.com/css2?family=Open+Sans:wght@300;400&display=swap">
<style>
  :root {
    --orange: #f7941d;
    --green: #3dba85;
    --mint-panel: #c8e6d5;
    --ink: #1a1a1a;
    --icon-grey: #9ea5a2;
    --rule-grey: #a3aaa6;
    --white: #ffffff;
  }
  html, body {
    margin: 0;
    padding: 0;
    overflow: hidden;
    background: var(--green);
  }
  .card {
    position: relative;
    width: 1200px;
    height: 741px;
    overflow: hidden;
    background: var(--green);
    font-family: "Open Sans", Arial, sans-serif;
  }
  .top-band {
    position: absolute;
    left: 0; top: 0;
    width: 1200px; height: 290px;
    background: var(--orange);
    box-shadow: 0 4px 8px rgba(0,0,0,0.18);
    z-index: 1;
  }
  .contact-panel {
    position: absolute;
    left: 0; top: 360px;
    width: 1146px; height: 329px;
    background: var(--mint-panel);
    z-index: 1;
  }
  .lens-decoration {
    position: absolute;
    left: -206px; top: 0;
    width: 692px; height: 692px;
    border-radius: 50%;
    background: radial-gradient(circle, rgba(255,255,255,0.55) 0%, rgba(255,255,255,0.25) 45%, rgba(255,255,255,0) 70%);
    z-index: 2;
  }
  .brand {
    position: absolute;
    left: 440px; top: 22px;
    width: 600px;
    color: var(--white);
    font-weight: 300;
    z-index: 3;
    text-align: center;
  }
  .brand-name {
    display: block;
    font-size: 104px;
    line-height: 1.05;
  }
  .brand-line {
    display: block;
    font-size: 78px;
    line-height: 1.05;
  }
  .brand-by {
    display: block;
    font-size: 38px;
    line-height: 1.1;
    text-align: right;
    padding-right: 30px;
  }
  .contact-row {
    position: absolute;
    left: 428px;
    display: flex;
    align-items: center;
    color: var(--ink);
    z-index: 3;
  }
  .contact-row svg {
    width: 32px; height: 32px;
    fill: var(--icon-grey);
    margin-right: 70px;
  }
  .contact-name {
    top: 418px;
    font-size: 33px;
    letter-spacing: 0.2em;
    font-weight: 400;
  }
  .contact-phone,
  .contact-place {
    font-size: 28px;
    letter-spacing: 0.1em;
    font-weight: 400;
  }
  .contact-phone { top: 550px; }
  .contact-place { top: 599px; }
  .divider {
    position: absolute;
    left: 338px; top: 502px;
    width: 779px; height: 2px;
    background: var(--rule-grey);
    z-index: 3;
  }
</style>
</head>
<body>
  <div class="card">
    <div class="top-band"></div>
    <div class="contact-panel"></div>
    <div class="lens-decoration" role="img" aria-label="Decorative camera-lens ornament with looping white lines"></div>

    <div class="brand">
      <span class="brand-name">Lumivale</span>
      <span class="brand-line">Photography</span>
      <span class="brand-by">by Tavi</span>
    </div>

    <div class="contact-row contact-name">
      <svg viewBox="0 0 24 24" aria-hidden="true"><circle cx="12" cy="8" r="4.5"/><path d="M3 21c0-4.5 4-7 9-7s9 2.5 9 7z"/></svg>
      <span>NORAH BALFREY</span>
    </div>

    <div class="divider"></div>

    <div class="contact-row contact-phone">
      <svg viewBox="0 0 24 24" aria-hidden="true"><path d="M6.6 10.8c1.4 2.8 3.8 5.1 6.6 6.6l2.2-2.2c.3-.3.7-.4 1-.2 1.1.4 2.3.6 3.6.6.6 0 1 .4 1 1V20c0 .6-.4 1-1 1C10.6 21 3 13.4 3 4c0-.6.4-1 1-1h3.5c.6 0 1 .4 1 1 0 1.3.2 2.5.6 3.6.1.3 0 .7-.2 1z"/></svg>
      <span>0487 356 024</span>
    </div>

    <div class="contact-row contact-place">
      <svg viewBox="0 0 24 24" aria-hidden="true"><path d="M4 3h16c.6 0 1 .4 1 1v12c0 .6-.4 1-1 1H8l-4 4V4c0-.6.4-1 1-1zm3 4v2h10V7zm0 4v2h7v-2z"/></svg>
      <span>KESTREL COVE, QUEENSLAND</span>
    </div>
  </div>
</body>
</html>
```